Cedar Hollow Business Card and Logo

Nutrition and Wellness Store Front. I sell supplements, herbs, tinctures, Loose Leaf Teas, natural snacks and drinks including gluten free. classes: Fitness; health and wellness; community health and wellness hub. It is a "shabby chic" store front. It is white and my accent color is turqouise I will be adding some jewelry, stones and rocks and jewelery. I am a Certified Herbalist and Certified Nutrition and Wellness Consultant, a Solvane Practitioner and Kavora instructor.

Target Market(s)

health and wellness seekers, fitness, baby boomer

Industry/Entity Type

Business

Contact Information for Business Card

Cedar Hollow Nutrition and Wellness
Marla Dunstable Certified Herbalist , Certified Nutrition and Wellness Consultant, Solvane Practitioner, Kavora Instructor

Font styles to use
Serif

Colors
33a6d7
3176b5
33b8a4

Requirements
Must have
• A picture that represents two mountain peaks with a floral accent.

```html
<!DOCTYPE html>
<html lang="en">
<head>
<meta charset="utf-8">
<title>Cedar Hollow Nutrition and Wellness – Business Card</title>
<link href="https://fonts.googleapis.com/css2?family=Open+Sans:wght@400;600;700&display=swap" rel="stylesheet">
<style>
  :root {
    --page: #eceae6;
    --teal: #1fb3c4;
    --teal-deep: #169fb0;
    --band-blue: #3d8fc0;
    --band-blue-soft: rgba(61, 143, 192, 0.82);
    --sky-pink: #d99ac4;
    --sky-violet: #9a7cc0;
    --meadow-green: #4f8a3c;
    --lupine: #7450b4;
    --white: #ffffff;
  }
  * { box-sizing: border-box; margin: 0; padding: 0; }
  html, body {
    width: 1200px; height: 1022px; overflow: hidden;
    background: var(--page);
    font-family: "Open Sans", Arial, sans-serif;
  }
  .sheet {
    width: 1200px; height: 1022px;
    display: flex; flex-direction: column; align-items: center;
    justify-content: center; gap: 30px;
  }
  .card {
    position: relative; width: 840px; height: 480px;
    border-radius: 18px; overflow: hidden;
    box-shadow: 0 6px 18px rgba(0,0,0,0.18);
  }
  .card-art { position: absolute; inset: 0; width: 100%; height: 100%; }

  .brand {
    position: absolute; left: 40px; top: 48px;
    display: flex; align-items: center; gap: 18px;
    color: var(--white);
  }
  .brand-dot {
    width: 70px; height: 70px; border-radius: 50%;
    border: 3px solid var(--white);
  }
  .brand-name {
    font-size: 26px; font-weight: 400; line-height: 1.25;
    width: 300px;
  }

  .holder {
    position: absolute; left: 40px; top: 208px; color: var(--white);
  }
  .holder-name { font-size: 40px; font-weight: 700; letter-spacing: 0.5px; }
  .holder-title { font-size: 22px; font-weight: 400; margin-top: 2px; }

  .services {
    position: absolute; left: 0; bottom: 0; width: 640px; height: 150px;
    background: var(--band-blue-soft);
    list-style: none; padding: 22px 0 0 40px; color: var(--white);
    font-size: 22px; line-height: 1.55;
  }
  .services li { display: flex; align-items: center; gap: 14px; }
  .tick { width: 18px; height: 18px; flex: none; }
</style>
</head>
<body>
<main class="sheet">

  <section class="card card-front">
    <svg class="card-art" viewBox="0 0 840 480" preserveAspectRatio="none">
      <defs>
        <linearGradient id="meadow" x1="0" y1="0" x2="0" y2="1">
          <stop offset="0" stop-color="var(--sky-pink)"/>
          <stop offset="0.3" stop-color="var(--sky-violet)"/>
          <stop offset="0.6" stop-color="var(--meadow-green)"/>
          <stop offset="1" stop-color="var(--lupine)"/>
        </linearGradient>
      </defs>
      <rect class="teal-field" width="840" height="480" fill="var(--teal)"/>
      <path role="img" aria-label="Photo of two snowy mountain peaks above a meadow of purple lupine wildflowers"
            d="M0 0 H600 C560 160 700 300 640 480 H0 Z" fill="url(#meadow)"/>
      <path class="wave-band" d="M600 0 C560 160 700 300 640 480"
            fill="none" stroke="var(--band-blue)" stroke-width="44"/>
    </svg>

    <div class="brand">
      <span class="brand-dot"></span>
      <span class="brand-name">Cedar Hollow Nutrition and Wellness</span>
    </div>

    <div class="holder">
      <h1 class="holder-name">Marla Dunstable</h1>
      <p class="holder-title">Certified Herbalist</p>
    </div>

    <ul class="services">
      <li><svg class="tick" viewBox="0 0 18 18"><path d="M2 9 L7 14 L16 3" fill="none" stroke="#fff" stroke-width="3"/></svg>Solvane Practitioner</li>
      <li><svg class="tick" viewBox="0 0 18 18"><path d="M2 9 L7 14 L16 3" fill="none" stroke="#fff" stroke-width="3"/></svg>Kavora Instructor</li>
      <li><svg class="tick" viewBox="0 0 18 18"><path d="M2 9 L7 14 L16 3" fill="none" stroke="#fff" stroke-width="3"/></svg>Certified Nutrition and Wellness Consultant</li>
    </ul>
  </section>

  <section class="card card-back">
    <svg class="card-art" viewBox="0 0 840 480" preserveAspectRatio="none">
      <defs>
        <linearGradient id="meadow-back" x1="0" y1="0" x2="0" y2="1">
          <stop offset="0" stop-color="var(--sky-pink)"/>
          <stop offset="0.45" stop-color="var(--sky-violet)"/>
          <stop offset="1" stop-color="var(--meadow-green)"/>
        </linearGradient>
      </defs>
      <rect class="teal-field" width="840" height="480" fill="var(--teal)"/>
      <path role="img" aria-label="Photo of mountain peaks at sunset above a wildflower meadow"
            d="M0 0 H460 A300 300 0 0 1 0 300 Z" fill="url(#meadow-back)"/>
      <path class="wave-band" d="M460 0 A300 300 0 0 1 0 300"
            fill="none" stroke="var(--band-blue)" stroke-width="44"/>
    </svg>
  </section>

</main>
</body>
</html>
```